Business Card Design Project

I need a business card for an environmentally friendly interior design company called Roomcraft Willow.
I was thinking it might be nice to print the business cards on brown recycled paper with green ink.
In addition to interior design, I will also be able to consult with homeowners regarding their indoor environments and how they might be affecting their health after May 2013 which is when I will complete my certification program. This can be added to the business card at that time: "Certified Habitat Vitalis Dwelling Consultant".
Health

```html
<!DOCTYPE html>
<html lang="en">
<head>
<meta charset="utf-8">
<title>Roomcraft Willow – Business Card</title>
<link href="https://fonts.googleapis.com/css2?family=Federant&family=Source+Sans+3:wght@400;700&display=swap" rel="stylesheet">
<style>
  :root {
    --paper-brown: #96520c;
    --leaf-lime: #cddc1a;
    --ink-green: #5aa51e;
    --title-green: #4a9a1c;
  }
  html, body {
    margin: 0;
    padding: 0;
    overflow: hidden;
    background: var(--paper-brown);
  }
  .card {
    position: relative;
    width: 1200px;
    height: 708px;
    background: var(--paper-brown);
    overflow: hidden;
    font-family: "Source Sans 3", "Myriad Pro", Arial, sans-serif;
    color: var(--ink-green);
  }
  .leaf-art {
    position: absolute;
    left: 0;
    top: 0;
    width: 1200px;
    height: 708px;
  }
  .brand-name {
    position: absolute;
    left: 58px;
    top: 22px;
    margin: 0;
    font-family: "Federant", "Georgia", serif;
    font-weight: 400;
    font-size: 72px;
    line-height: 1;
    color: var(--title-green);
    letter-spacing: 1px;
  }
  .service {
    position: absolute;
    left: 56px;
    margin: 0;
    font-size: 46px;
    line-height: 64px;
    font-weight: 400;
  }
  .service--design { top: 170px; }
  .service--consult { top: 252px; }
  .contact {
    position: absolute;
    left: 58px;
    top: 522px;
    margin: 0;
    font-size: 41px;
    line-height: 60px;
    font-weight: 700;
  }
  .contact span { display: block; }
</style>
</head>
<body>
  <div class="card">
    <svg class="leaf-art" viewBox="0 0 1200 708" role="img" aria-label="Large stylised lime-green leaf illustration sweeping across the card">
      <defs>
        <radialGradient id="leafGlow" cx="0.55" cy="0.5" r="0.5">
          <stop offset="0" stop-color="#cddc1a"/>
          <stop offset="0.7" stop-color="#cddc1a" stop-opacity="0.85"/>
          <stop offset="1" stop-color="#96520c" stop-opacity="0"/>
        </radialGradient>
      </defs>
      <ellipse cx="600" cy="370" rx="560" ry="320" fill="url(#leafGlow)"/>
    </svg>

    <h1 class="brand-name">Roomcraft Willow</h1>
    <p class="service service--design">Environmentally friendly design</p>
    <p class="service service--consult">Certified Habitat Vitalis Dwelling<br>Consultant</p>

    <p class="contact">
      <span class="contact-name">Lena Marsh Avery</span>
      <span class="contact-phone">713-555-0148</span>
    </p>
  </div>
</body>
</html>
```